Bright Meadow Co - labels

I have my logo now so its time to proceed with the labels.
The product is organic juices and smoothies. They will be served in Mason jar's and sold as a premium hand made product into the CBD and outlets around Perth such as yoga studios gyms, cafe's etc. Cleanses to individuals etc.
I have attached the logo and a mock of what I would like to see.
I think the logo and the raw organic, handmade look will work with the Chalkboard design and maybe some bunting to brighten the design.
There is currently approx. 10 Juices and Smoothies to the range so I will need to settle on the design and then have you create a label for each one, once settled on the design.
If you have any questions please let me know.

Text on label:
Raw, Organic, Hand Made, Gluten-Free, Dairy-Free

Juice
Morning Vital Sip
Kale, Apple, Celery, Dandelion, Lemon & Ginger

This product is FRESH. Shake before you enjoy!!!

Label size. highest point for height 70 - 75mm. Length 200mm
I also have more wording and nutritional guide for Australian Standards. I will update soon.
Thank you

    Happy Friday Designers!!!

Well I have just increased the budget to $300. I hope this helps to get some designs coming through. If you need anything else from me please send a message.

I look forward to receiving your designs soon and thank you for working with me on my business. this is such an exciting time for me and you guys are making my dream a reality so thank you for your time.

Regards,

Tamsin

Reason: I have not received many designs so extending for a few more days.

Cafe

• Wording - Hand Made
Raw, Organic, Gluten-Free, Dairy-Free
• A chalk board with Juice or Smoothie - Name and ingredients
Bunting I think will work well with the design of logo and chalk board plus bring some colour.

```html
<!DOCTYPE html>
<html lang="en">
<head>
<meta charset="utf-8">
<title>Bright Meadow Co – Jar Label</title>
<link href="https://fonts.googleapis.com/css2?family=Cabin+Sketch&family=Patrick+Hand+SC&display=swap" rel="stylesheet">
<style>
  :root {
    --backdrop-light: #c9d8e0;
    --backdrop-dark: #a9bfcb;
    --label-white: #ffffff;
    --label-yellow: #dde21f;
    --label-green: #1f9a3d;
    --chalk-centre: #3b3b3b;
    --chalk-edge: #1d1d1d;
    --chalk-yellow: #d8de2b;
    --chalk-white: #f2f2f2;
    --tick-red: #e2262b;
  }
  * { box-sizing: border-box; margin: 0; padding: 0; }
  html, body { width: 1200px; height: 563px; overflow: hidden; }
  body {
    background: linear-gradient(160deg, var(--backdrop-light), var(--backdrop-dark));
    font-family: "Patrick Hand SC", cursive;
  }
  .label-sheet { position: relative; width: 1200px; height: 563px; overflow: hidden; }
  .label-shapes { position: absolute; inset: 0; }
  .panel-heading {
    position: absolute; top: 210px; width: 300px;
    text-align: center; color: var(--chalk-yellow); font-size: 13px; font-weight: 400; letter-spacing: 0.3px;
  }
  .panel-heading--story { left: 90px; }
  .panel-heading--nutrition { left: 828px; }
  .brand-name {
    position: absolute; left: 525px; top: 104px; width: 180px;
    text-align: center; color: var(--label-white); font-size: 30px; line-height: 34px;
  }
  .product-name {
    position: absolute; left: 470px; top: 263px; width: 290px;
    text-align: center; white-space: nowrap; font-family: "Cabin Sketch", cursive;
    font-size: 30px; font-weight: 400; line-height: 38px;
    color: var(--chalk-yellow); letter-spacing: 0;
  }
  .ingredients {
    position: absolute; left: 497px; top: 348px; width: 236px;
    text-align: center; white-space: nowrap; color: var(--chalk-yellow); font-size: 11px; letter-spacing: 0;
  }
  .claims {
    position: absolute; left: 465px; width: 300px; list-style: none;
    display: flex; justify-content: center; gap: 16px;
    color: var(--chalk-white); font-size: 14px;
  }
  .claims--first { top: 397px; }
  .claims--second { top: 420px; gap: 8px; }
  .claim { display: flex; align-items: center; gap: 2px; }
  .claim svg { width: 14px; height: 14px; }
  .freshness-note {
    position: absolute; left: 465px; top: 455px; width: 300px;
    text-align: center; white-space: nowrap; color: var(--chalk-yellow); font-size: 12px;
  }
  .freshness-note strong { color: var(--tick-red); font-weight: 400; }
</style>
</head>
<body>
<main class="label-sheet">
  <svg class="label-shapes" width="1200" height="563" viewBox="0 0 1200 563" aria-hidden="true">
    <defs>
      <radialGradient id="chalkboard" cx="50%" cy="50%" r="70%">
        <stop offset="0" stop-color="var(--chalk-centre)"/>
        <stop offset="1" stop-color="var(--chalk-edge)"/>
      </radialGradient>
      <g id="side-panel">
        <path fill="var(--label-white)" d="M98,180 L416,180 L416,461 L98,461 A38 38 0 0 0 60,423 L60,218 A38 38 0 0 0 98,180 Z"/>
        <path fill="var(--label-yellow)" d="M102,184 L412,184 L412,457 L102,457 A38 38 0 0 0 64,419 L64,222 A38 38 0 0 0 102,184 Z"/>
        <path fill="var(--label-white)" d="M113,195 L401,195 L401,446 L113,446 A38 38 0 0 0 75,408 L75,233 A38 38 0 0 0 113,195 Z"/>
        <path fill="var(--label-green)" d="M116,198 L398,198 L398,443 L116,443 A38 38 0 0 0 78,405 L78,236 A38 38 0 0 0 116,198 Z"/>
        <path fill="var(--label-white)" d="M120,202 L394,202 L394,439 L120,439 A38 38 0 0 0 82,401 L82,240 A38 38 0 0 0 120,202 Z"/>
        <path fill="url(#chalkboard)" d="M124,206 L390,206 L390,435 L124,435 A38 38 0 0 0 86,397 L86,244 A38 38 0 0 0 124,206 Z"/>
      </g>
    </defs>

    <use href="#side-panel"/>
    <use href="#side-panel" transform="translate(1230,0) scale(-1,1)"/>

    <path fill="var(--label-white)" d="M440,500 L440,215 A38 38 0 0 0 478,177 L478,120 C478,60 545,20 615,20 C685,20 752,60 752,120 L752,177 A38 38 0 0 0 790,215 L790,500 Z"/>
    <path fill="var(--label-yellow)" d="M444,496 L444,219 A38 38 0 0 0 482,181 L482,120 C482,64 545,24 615,24 C685,24 748,64 748,120 L748,181 A38 38 0 0 0 786,219 L786,496 Z"/>
    <path fill="var(--label-white)" d="M455,485 L455,230 A38 38 0 0 0 493,192 L493,120 C493,75 548,35 615,35 C682,35 737,75 737,120 L737,192 A38 38 0 0 0 775,230 L775,485 Z"/>
    <path fill="var(--label-green)" d="M458,482 L458,233 A38 38 0 0 0 496,195 L496,120 C496,78 549,38 615,38 C681,38 734,78 734,120 L734,195 A38 38 0 0 0 772,233 L772,482 Z"/>
    <path fill="var(--label-white)" d="M462,478 L462,237 A38 38 0 0 0 500,199 L500,120 C500,82 550,42 615,42 C680,42 730,82 730,120 L730,199 A38 38 0 0 0 768,237 L768,478 Z"/>
    <path fill="url(#chalkboard)" d="M466,474 L466,241 A38 38 0 0 0 504,203 L504,120 C504,86 551,46 615,46 C679,46 726,86 726,120 L726,203 A38 38 0 0 0 764,241 L764,474 Z"/>

    <circle cx="615" cy="140" r="90" fill="var(--label-yellow)"/>

    <rect x="480" y="313" width="118" height="12" rx="6" fill="var(--chalk-white)" opacity="0.35" role="img" aria-label="Chalk-drawn flourish, left"/>
    <rect x="632" y="313" width="118" height="12" rx="6" fill="var(--chalk-white)" opacity="0.35" role="img" aria-label="Chalk-drawn flourish, right"/>

    <polygon points="472,350 497,350 497,378 486,378 472,378 480,364" fill="none" stroke="var(--chalk-white)" stroke-width="1.5"/>
    <polygon points="758,350 733,350 733,378 744,378 758,378 750,364" fill="none" stroke="var(--chalk-white)" stroke-width="1.5"/>
    <rect x="497" y="341" width="236" height="30" fill="#262626" stroke="var(--chalk-white)" stroke-width="1.5"/>
  </svg>

  <h2 class="panel-heading panel-heading--story">OUR STORY OR DIRECTIONS</h2>
  <h2 class="panel-heading panel-heading--nutrition">NUTRITIONAL INFOMATION</h2>

  <p class="brand-name">BRIGHT<br>MEADOW CO</p>
  <h1 class="product-name">MORNING VITAL SIP</h1>
  <p class="ingredients">KALE, APPLE, CELERY, DANDELION, LEMON &amp; GINGER</p>

  <ul class="claims claims--first">
    <li class="claim"><svg viewBox="0 0 14 14"><path d="M1,7 L5,12 L13,1" fill="none" stroke="var(--tick-red)" stroke-width="2.6" stroke-linecap="round"/></svg>RAW</li>
    <li class="claim"><svg viewBox="0 0 14 14"><path d="M1,7 L5,12 L13,1" fill="none" stroke="var(--tick-red)" stroke-width="2.6" stroke-linecap="round"/></svg>HAND MADE</li>
    <li class="claim"><svg viewBox="0 0 14 14"><path d="M1,7 L5,12 L13,1" fill="none" stroke="var(--tick-red)" stroke-width="2.6" stroke-linecap="round"/></svg>ORGANIC</li>
  </ul>
  <ul class="claims claims--second">
    <li class="claim"><svg viewBox="0 0 14 14"><path d="M1,7 L5,12 L13,1" fill="none" stroke="var(--tick-red)" stroke-width="2.6" stroke-linecap="round"/></svg>DAIRY-FREE</li>
    <li class="claim"><svg viewBox="0 0 14 14"><path d="M1,7 L5,12 L13,1" fill="none" stroke="var(--tick-red)" stroke-width="2.6" stroke-linecap="round"/></svg>GLUTEN-FREE</li>
  </ul>

  <p class="freshness-note">This product is <strong>FRESH</strong>. Shake before you enjoy!!!</p>
</main>
</body>
</html>
```